I am looking to have decal designs made that I can wrap the body of a plastic lighter with. I have included the lighter design template with the specific size of decal needed, including cut-out. The lighter is 3.25" tall and 1" wide and will be wrapped in a decal the size of the template.

These are separate and distinct lighters, but come from the same company, so a similar "feel" isn't a bad thing. Please submit separate designs, it's easier to give feedback that way.

1. The first lighter is called an "Marble Bay" Flame and is targeted at tourists visiting Seattle. Please note that the Cobalt Spire is a trademarked image, even stylized representations of it cannot be used. I am open to creativity, but simple is best, while eye-catching. It can say Seattle on the opposite side from Marble Bay, that's fine. But don't let me limit you. Regardless, it is intended to catch the eye and be somewhat of an impulse buy in tourist shops. But I won't sell eye-sores. The lighter trigger is a translucent green and glows in the dark. Some are black, with black bodies.

2. The second lighter is called a "88Drift" and is as you might have suspected, targeted at the cannabis crowd, both smoke shops and end users. The lighter trigger is a translucent green and glows in the dark for these as well. Lighter body is black, but that can be changed to match your design if warranted. I want 88Drift to be very legible. See below for the "brand band" I'm looking for incorporating my logo on each lighter. What to put on the back side of this lighter (the decal is a full wrap) is up to you, but I want pot smokers to enjoy using the lighter. Pot leaves, whatever, but with most things, I do like a simple, clean, smooth look. Polished you might say.

For both lighters, my company name is "CopperWren" with no space. I would like my logo (included file) and company name incorporated into the design of both lighters. Please choose a font for the company name that "suits" the logo (I call him Otis). Otis can be any color, doesn't have to be white, that's just the typical / default and it looks good on a number of background colors.

3. Based on the above, please note that I'd like a "default" CopperWren lighter decal made as well. Same product as the above, but not a 88 or Marble Bay. This can be similar to the other two, but the only wording on there will be the company name. That and Otis, the logo. I want to focus on the first two lighters and then create the 3rd one once the others are finalized.

Please let me know if you have any questions.

Target Market(s)

1. tourists visiting Seattle, so the lighters will be sold to retail shops

2. any marijuana user, dispensary, smoke shop, etc.

Industry/Entity Type

Plastic

Requirements
Must have
• 1. Marble Bay very legible
- targeted to Seattle tourists

2. 88Drift very legible
- targeted to pot consumers

3. The color green in each lighter design

4. A font for "CopperWren" that is usable on website, product, apparel, stickers, etc.
- the font should "suit" Otis and have the same company feel, fun and joyful
Nice to have
• A full wrap design, not segmented
Attractive image, fun to carry around
Should not have
• Emphasis specifically on the Cobalt Spire

```html
<!DOCTYPE html>
<html lang="en">
<head>
<meta charset="utf-8">
<title>CopperWren Lighter Wraps</title>
<link rel="stylesheet" href="https://fonts.googleapis.com/css2?family=Bebas+Neue&family=Oswald:wght@400;700&display=swap">
<style>
  :root {
    --page: #ffffff;
    --sky: #22a9e1;
    --sky-deep: #1e9fd6;
    --strip-line-blue: #2a6fa8;
    --strip-line-pink: #e0407a;
    --lime-top: #cadc28;
    --lime-bottom: #7ec242;
    --crystal-light: #eef2a8;
    --crystal-dark: #a9b62c;
    --ink: #111111;
    --white: #ffffff;
    --mark-blue: #a9d6f2;
    --mark-lime: #e4f0b4;
  }
  * { box-sizing: border-box; margin: 0; padding: 0; }
  html, body { width: 1200px; height: 630px; overflow: hidden; background: var(--page); }
  .canvas { position: relative; width: 1200px; height: 630px; }

  .wrap { position: absolute; top: 10px; height: 612px; overflow: hidden; }
  .wrap--marble { left: 8px; width: 565px; background: var(--sky); }
  .wrap--drift { left: 625px; width: 565px; background: linear-gradient(180deg, var(--lime-top), var(--lime-bottom)); }

  .cut-strip { position: absolute; top: 0; height: 612px; }
  .wrap--marble .cut-strip { left: 192px; width: 181px; background: var(--sky-deep); border-left: 1px solid var(--strip-line-blue); border-right: 1px solid var(--strip-line-blue); }
  .wrap--drift .cut-strip { left: 185px; width: 200px; border: 1px solid var(--strip-line-pink); }

  .crystal { position: absolute; top: 108px; width: 172px; height: 195px;
    border-radius: 40% 40% 18% 18%;
    background: radial-gradient(circle at 50% 40%, var(--crystal-light), var(--crystal-dark)); }
  .crystal--front { left: 6px; }
  .crystal--back { left: 388px; }

  .city-name { position: absolute; top: 336px; width: 180px; text-align: center;
    font-family: "Bebas Neue", "Oswald", sans-serif; font-weight: 400; color: var(--white);
    line-height: 0.9; text-shadow: 0 3px 4px rgba(0,0,0,.35); }
  .city-name--front { left: 0; }
  .city-name--back { left: 384px; }
  .city-name__top { display: block; font-size: 46px; }
  .city-name__bottom { display: block; font-size: 62px; }

  .maker-name { position: absolute; top: 520px; width: 180px; text-align: center;
    font-family: "Oswald", sans-serif; font-weight: 700; font-size: 20px; letter-spacing: .5px; }
  .wrap--marble .maker-name { color: var(--mark-blue); }
  .wrap--drift .maker-name { color: var(--mark-lime); }
  .maker-name--front { left: 0; }
  .maker-name--center { left: 195px; }
  .maker-name--back { left: 384px; }

  .flame-emblem { position: absolute; top: 24px; width: 150px; height: 230px;
    border-radius: 50% 50% 45% 45%;
    background: linear-gradient(160deg, #3a3a3a, var(--ink) 60%); }
  .flame-emblem--front { left: 10px; }
  .flame-emblem--back { left: 395px; }

  .product-name { position: absolute; top: 392px; width: 316px; height: 80px;
    transform: rotate(-90deg); transform-origin: center;
    font-family: "Oswald", sans-serif; font-size: 84px; line-height: 80px;
    text-transform: uppercase; text-align: center; white-space: nowrap; }
  .product-name--front { left: -75px; }
  .product-name--back { left: 310px; }
  .product-name__number { color: var(--white); font-weight: 400; }
  .product-name__word { color: var(--ink); font-weight: 700; }
</style>
</head>
<body>
<main class="canvas">

  <section class="wrap wrap--marble" aria-label="Marble Bay lighter wrap">
    <div class="cut-strip"></div>

    <div class="crystal crystal--front" role="img" aria-label="Illustration of yellow-green crystals"></div>
    <h1 class="city-name city-name--front"><span class="city-name__top">Marble</span><span class="city-name__bottom">Bay</span></h1>
    <p class="maker-name maker-name--front">CopperWren</p>

    <div class="crystal crystal--back" role="img" aria-label="Illustration of yellow-green crystals"></div>
    <p class="city-name city-name--back"><span class="city-name__top">Marble</span><span class="city-name__bottom">Bay</span></p>
    <p class="maker-name maker-name--back">CopperWren</p>
  </section>

  <section class="wrap wrap--drift" aria-label="88Drift lighter wrap">
    <div class="cut-strip"></div>

    <div class="flame-emblem flame-emblem--front" role="img" aria-label="Black flame emblem"></div>
    <h2 class="product-name product-name--front"><span class="product-name__number">88</span><span class="product-name__word">Drift</span></h2>

    <p class="maker-name maker-name--center">CopperWren</p>

    <div class="flame-emblem flame-emblem--back" role="img" aria-label="Black flame emblem"></div>
    <p class="product-name product-name--back"><span class="product-name__number">88</span><span class="product-name__word">Drift</span></p>
  </section>

</main>
</body>
</html>
```